Vitoplume.com

I need a web design for a Online Wellness Center based in Chicago, IL and it's called "Vitoplume" We provide Health risk assessment to individuals and interventions. Our portal has a Health Activity tracker where our members record health activities and aerobic miles and biometric data. Our Online wellness center tracks the participant's progress toward health goals and awards points for completed activities.
I started working on this website but the designer was not able to designer a website which describes what we do. I need a fresh look on this project. I need a very attractive, responsive website which says what we do.
These are the things we do.
1. We provide Health Risk Assessments to individuals and Co-operations
2. We Provide Free health screenings to undeserved communities
3. Assist individuals access free or affordable medications
4. We ask providers/doctors to see (or do a complete physical) one individual free of charge once a year (those individuals who are no insured and don't have money to pay from their pocket)
5. Assist patient access lab work at low cost
Our goal is to provide services that will lower the cost of care for our members.

Here is the website: www.vitoplume.com still underdevelopment. PLEASE DO NOT COPY THIS STYLE OF WEBSITE. IT'S A BAD DESIGN AND THAT IS WHY I'M RE-DESIGNING THE SITE

Target Market(s)

Health individuals between the age of 21 to 65 Plus years old. Insured and uninsured

Industry/Entity Type

Health And Wellness

Coding

Coded - Design and coding required

Number of Pages Required

5+ page

Colors
0292cd

Requirements
Must have
• I'm still working on this websiteHere is the menu: Home, About us, Services, Health Screening, Providers, Contacts
• Please see. www.vitoplume.com
Nice to have
• Event calender
• Upcoming Event
• Medication
• Lab assist
• Providers/Free Clinics

```html
<!DOCTYPE html>
<html lang="en">
<head>
<meta charset="utf-8">
<title>Vitoplume – Online Wellness Center</title>
<link rel="stylesheet" href="https://fonts.googleapis.com/css2?family=Open+Sans:wght@400;600;700&family=Playfair+Display:wght@700&display=swap">
<style>
:root{
  --brand:#0292cd;
  --brand-dark:#0a6fa3;
  --navy:#1e3a6e;
  --green:#4aa83c;
  --red:#d4262c;
  --grey:#7d8388;
  --ink:#333;
  --muted:#777;
  --light:#f3f5f7;
  --footer:#2b2b2b;
  --white:#fff;
}
*{box-sizing:border-box;margin:0;padding:0}
html,body{width:1200px;height:3512px;overflow:hidden}
body{font-family:"Open Sans",Arial,sans-serif;color:var(--ink);background:var(--white);position:relative;font-size:14px}
.abs{position:absolute}
.serif{font-family:"Playfair Display",Georgia,serif}

/* header */
.topline{top:0;left:0;width:1200px;height:40px}
.socials{left:270px;top:10px;display:flex;gap:8px}
.socials span{width:20px;height:20px;border-radius:50%;background:var(--brand);display:block}
.search{left:615px;top:10px;width:170px;height:20px;background:var(--brand);border-radius:2px;color:#d8efff;font-size:10px;padding:3px 8px}
.masthead{top:40px;left:0;width:1200px;height:80px}
.mail{left:220px;top:30px;font-size:12px;color:var(--muted);display:flex;align-items:center;gap:10px}
.mail i{width:18px;height:18px;border:1px solid #bbb;border-radius:50%;display:block}
.brandname{left:500px;top:18px;display:flex;align-items:center;gap:10px}
.brandname i{width:30px;height:30px;border-radius:50%;background:var(--green);display:block}
.brandname b{font-size:32px;font-weight:700;color:var(--brand);letter-spacing:-.5px}
.call{left:850px;top:30px;font-size:12px;color:var(--muted);display:flex;align-items:center;gap:8px}
.call i{width:18px;height:18px;border:1px solid #bbb;border-radius:50%;display:block}
.nav{top:120px;left:0;width:1200px;height:32px;background:var(--brand)}
.nav ul{list-style:none;display:flex;justify-content:center;gap:34px;height:32px;align-items:center}
.nav li{color:#fff;font-size:12px;font-weight:600}
.nav li.on{background:var(--brand-dark);padding:8px 10px}
.dropdown{top:152px;left:580px;width:135px;background:#fff;box-shadow:0 2px 6px rgba(0,0,0,.25);z-index:5}
.dropdown div{font-size:10px;color:#555;padding:5px 10px;border-bottom:1px solid #eee}

/* hero */
.hero{top:152px;left:0;width:1200px;height:360px;background:linear-gradient(160deg,#9fcf4c,#6aa92e 55%,#4f8e23)}
.hero-center{left:440px;top:30px;width:320px;height:330px;background:radial-gradient(circle at 50% 45%,#e6d6c4,#b8c98c 70%,transparent 72%)}
.pill{font-size:20px;font-weight:700;color:#fff;letter-spacing:1px}
.bubble{width:92px;height:92px;border-radius:50%;background:radial-gradient(circle,#f2efe9,#c9d8c2);border:4px solid #fff}
.arrow{width:40px;height:40px;background:rgba(0,0,0,.35);top:160px;color:#fff;font-size:22px;text-align:center;line-height:40px}

/* service tiles */
.tiles{top:605px;left:172px;width:860px;height:600px;display:grid;grid-template-columns:repeat(3,1fr);grid-template-rows:300px 300px}
.tile{position:relative;color:#fff;text-align:center;padding:18px 26px}
.tile h3{font-size:22px;font-weight:600;margin-bottom:12px}
.tile p{font-size:10px;line-height:1.5;opacity:.9}
.tile .btn{display:inline-block;margin-top:14px;font-size:10px;border:1px solid #fff;padding:5px 16px}
.t-med{background:var(--brand)}
.t-cal{background:var(--grey);padding:0}
.t-lab{background:var(--green)}
.t-event{background:linear-gradient(150deg,#6b8fa8,#334e62)}
.t-prov{background:var(--navy)}
.t-track{background:var(--red)}
.icon{width:70px;height:70px;margin:0 auto 8px}
.cal-head{background:#5d6368;font-size:22px;padding:10px 0}
.cal-month{background:var(--brand);width:220px;margin:12px auto 0;font-size:13px;padding:5px 0;display:flex;justify-content:space-between;padding:5px 10px}
.cal{width:220px;margin:0 auto;border-collapse:collapse;background:#fff;color:#555;font-size:10px}
.cal td,.cal th{border:1px solid #ddd;height:24px;text-align:center}
.cal th{background:#eee;font-weight:600}
.cal td.today{background:var(--brand);color:#fff}
.cal td.dim{color:#bbb}
.band{position:absolute;left:0;bottom:0;width:100%;background:rgba(0,0,0,.45);padding:10px;font-size:20px}
.stats{position:absolute;left:14px;right:14px;bottom:16px;display:flex;justify-content:space-between;font-size:30px;font-weight:300}

/* things we do */
.things{top:1220px;left:0;width:1200px;height:420px;background:var(--brand);color:#fff;text-align:center}
.things h2{font-size:32px;margin-top:36px}
.rule{width:60px;height:2px;background:#fff;margin:12px auto}
.things .lead{font-size:12px;line-height:1.6;width:560px;margin:0 auto}
.do-row{display:flex;gap:12px;width:860px;margin:44px auto 0}
.do{flex:1;background:#fff;color:#555;height:140px;padding:14px 10px;font-size:9px;line-height:1.4;text-transform:uppercase;position:relative}
.do svg{width:36px;height:36px;margin-bottom:6px}
.do .mini{position:absolute;left:50%;bottom:12px;transform:translateX(-50%);background:var(--brand);color:#fff;padding:3px 12px;text-transform:none}
.do .mini.dark{background:#333}

/* programs */
.programs{top:1660px;left:0;width:1200px;height:440px;background:var(--light);text-align:center}
.programs h2{font-size:30px;color:var(--brand);margin-top:20px}
.programs .lead{font-size:12px;line-height:1.6;width:620px;margin:10px auto 0;color:#555;font-weight:600}
.prog-row{display:flex;gap:14px;width:860px;margin:32px auto 0}
.prog{flex:1;background:#fff;border:1px solid #ddd;height:190px}
.prog h4{background:var(--brand);color:#fff;font-size:13px;padding:5px 0;font-weight:600}
.prog .ph{height:66px;margin:6px}
.prog p{font-size:9px;color:#666;line-height:1.4;padding:2px 8px}
.prog .mini{display:inline-block;background:var(--brand);color:#fff;font-size:9px;padding:3px 12px;margin-top:6px}
.prog .mini.dark{background:#333}

/* events */
.events{top:2120px;left:0;width:1200px;height:460px;text-align:center}
.events h2{font-size:32px;color:var(--brand);margin-top:20px}
.ev-row{display:flex;gap:30px;width:860px;margin:40px auto 0}
.ev{flex:1;text-align:center}
.ev .ph{height:150px}
.ev h3{font-size:20px;color:var(--brand);margin:14px 0 8px}
.ev p{font-size:10px;color:#666;line-height:1.5;padding:0 6px}
.ev-meta{display:flex;justify-content:space-between;font-size:10px;color:#999;border-top:1px solid #ddd;margin-top:14px;padding-top:8px}

/* consultation */
.consult{top:2590px;left:0;width:600px;height:310px;background:var(--brand);color:#fff}
.consult .sub{position:absolute;left:175px;top:40px;font-size:12px;opacity:.85}
.consult h2{position:absolute;left:175px;top:60px;font-size:34px}
.consult label{position:absolute;left:175px;top:128px;font-size:11px}
.consult .field{position:absolute;left:175px;top:148px;width:330px;height:30px;background:#fff}
.consult .go{position:absolute;left:175px;top:200px;border:1px solid #fff;font-size:11px;padding:9px 22px}
.consult-photo{top:2590px;left:600px;width:600px;height:310px;background:linear-gradient(120deg,#f3f3f3,#d6e4ee 50%,#b9c8d6)}

/* contact */
.contact{top:2920px;left:0;width:1200px;height:480px}
.map{left:240px;top:30px;width:380px;height:360px;background:linear-gradient(135deg,#e9e6df,#d4d1c6)}
.contact .info{left:600px;top:40px;width:360px}
.contact h2{font-size:28px;color:var(--brand);font-weight:600}
.contact .info p{font-size:11px;color:#666;line-height:1.6;margin-top:8px}
.line{display:flex;gap:10px;font-size:11px;color:#555;margin-top:14px;align-items:flex-start}
.line svg{width:14px;height:14px;flex:none;margin-top:2px}
.footer{top:3408px;left:0;width:1200px;height:104px;background:var(--footer);color:#aaa}
.footer .fname{position:absolute;left:175px;top:38px;font-size:26px;font-weight:700;color:#666}
.footer .copy{position:absolute;left:575px;top:46px;font-size:10px}
.footer .up{position:absolute;left:990px;top:38px;width:30px;height:30px;border-radius:50%;border:1px solid #777}
</style>
</head>
<body>

<header>
  <div class="abs topline">
    <div class="abs socials"><span></span><span></span><span></span><span></span><span></span><span></span></div>
    <div class="abs search">Search…</div>
  </div>
  <div class="abs masthead">
    <div class="abs mail"><i></i>hello@vitoplume.com</div>
    <div class="abs brandname"><i></i><b>Vitoplume</b></div>
    <div class="abs call"><i></i>Call us Today: +1 (312) 555-0148</div>
  </div>
  <nav class="abs nav">
    <ul><li>Home</li><li>About us</li><li>Services</li><li class="on">Health Screening</li><li>Providers</li><li>Contacts</li></ul>
  </nav>
  <div class="abs dropdown">
    <div>Blood Pressure</div><div>Cholesterol Check</div><div>Glucose Screening</div><div>Body Mass Index</div><div>Vision Check</div><div>Flu Shots</div>
  </div>
</header>

<section class="abs hero" role="img" aria-label="Green banner with a smiling woman with arms raised and small round photos of wellness activities">
  <div class="abs hero-center"></div>
  <div class="abs pill" style="left:230px;top:85px">INTERVENE</div>
  <div class="abs bubble" style="left:350px;top:45px"></div>
  <div class="abs pill" style="left:800px;top:85px">MOTIVATE</div>
  <div class="abs bubble" style="left:730px;top:10px"></div>
  <div class="abs pill" style="left:225px;top:185px">DISCOVER</div>
  <div class="abs bubble" style="left:340px;top:160px"></div>
  <div class="abs pill" style="left:835px;top:185px">TRACK</div>
  <div class="abs bubble" style="left:755px;top:155px"></div>
  <div class="abs pill" style="left:250px;top:285px">ASSESS</div>
  <div class="abs bubble" style="left:340px;top:255px"></div>
  <div class="abs pill" style="left:860px;top:285px">MEASURE</div>
  <div class="abs bubble" style="left:760px;top:255px"></div>
  <div class="abs arrow" style="left:40px">‹</div>
  <div class="abs arrow" style="left:1120px">›</div>
</section>

<section class="abs tiles">
  <div class="tile t-med">
    <h3>Medication</h3>
    <svg class="icon" viewBox="0 0 70 70"><rect x="20" y="14" width="30" height="44" rx="4" fill="none" stroke="#fff" stroke-width="3"/><rect x="17" y="8" width="36" height="8" fill="#fff"/><path d="M35 28v16M27 36h16" stroke="#fff" stroke-width="4"/></svg>
    <p>Find affordable and free medicine options near you with our pharmacy partners and savings programs.</p>
    <span class="btn">READ MORE</span>
  </div>
  <div class="tile t-cal">
    <div class="cal-head">Event Calendar</div>
    <div class="cal-month"><span>‹</span><span>September 2015</span><span>›</span></div>
    <table class="cal">
      <tr><th>Su</th><th>Mo</th><th>Tu</th><th>We</th><th>Th</th><th>Fr</th><th>Sa</th></tr>
      <tr><td class="dim">30</td><td class="dim">31</td><td>1</td><td>2</td><td>3</td><td>4</td><td>5</td></tr>
      <tr><td>6</td><td>7</td><td>8</td><td>9</td><td>10</td><td>11</td><td>12</td></tr>
      <tr><td>13</td><td class="today">14</td><td>15</td><td>16</td><td>17</td><td>18</td><td>19</td></tr>
      <tr><td>20</td><td>21</td><td>22</td><td>23</td><td>24</td><td>25</td><td>26</td></tr>
      <tr><td>27</td><td>28</td><td>29</td><td>30</td><td class="dim">1</td><td class="dim">2</td><td class="dim">3</td></tr>
    </table>
  </div>
  <div class="tile t-lab">
    <h3>Lab Assist</h3>
    <svg class="icon" viewBox="0 0 70 70"><circle cx="35" cy="22" r="12" fill="#fff"/><path d="M14 62c0-14 9-24 21-24s21 10 21 24z" fill="#fff"/><path d="M30 44v10M25 49h10" stroke="#4aa83c" stroke-width="3"/></svg>
    <p>Get low cost lab work at partner labs across the city with simple online booking and results.</p>
    <span class="btn">READ MORE</span>
  </div>
  <div class="tile t-event" role="img" aria-label="Photo of people at a community health screening event">
    <div class="band">Upcoming Event</div>
  </div>
  <div class="tile t-prov">
    <h3>Providers / Free Clinics</h3>
    <svg class="icon" viewBox="0 0 70 70"><rect x="12" y="20" width="46" height="36" rx="3" fill="none" stroke="#fff" stroke-width="3"/><path d="M35 28v20M25 38h20" stroke="#fff" stroke-width="4"/><path d="M26 20v-6h18v6" fill="none" stroke="#fff" stroke-width="3"/></svg>
    <p>Some providers see one uninsured member free each year for a complete physical exam.</p>
    <span class="btn">READ MORE</span>
  </div>
  <div class="tile t-track">
    <h3>Health Activity Tracker</h3>
    <svg width="230" height="130" viewBox="0 0 230 130">
      <g fill="#8b0f14">
        <rect x="4" y="70" width="12" height="60"/><rect x="20" y="50" width="12" height="80"/><rect x="36" y="80" width="12" height="50"/><rect x="52" y="40" width="12" height="90"/><rect x="68" y="60" width="12" height="70"/><rect x="84" y="30" width="12" height="100"/><rect x="100" y="55" width="12" height="75"/><rect x="116" y="20" width="12" height="110"/><rect x="132" y="45" width="12" height="85"/><rect x="148" y="65" width="12" height="65"/><rect x="164" y="35" width="12" height="95"/><rect x="180" y="50" width="12" height="80"/><rect x="196" y="25" width="12" height="105"/><rect x="212" y="60" width="12" height="70"/>
      </g>
    </svg>
    <div class="stats"><span>1.25</span><span>1.00</span><span>0.25</span></div>
  </div>
</section>

<section class="abs things">
  <h2 class="serif">Things we do</h2>
  <div class="rule"></div>
  <p class="lead">Our commitment to serving everyone starts with lowering the cost of care for members through prevention, access and support.</p>
  <div class="do-row">
    <div class="do"><svg viewBox="0 0 36 36"><rect x="6" y="4" width="24" height="28" rx="2" fill="none" stroke="#0292cd" stroke-width="2"/><path d="M11 18l5 5 9-10" fill="none" stroke="#0292cd" stroke-width="2.5"/></svg><br>Health risk assessments for individuals<span class="mini">Read more</span></div>
    <div class="do"><svg viewBox="0 0 36 36"><path d="M18 31S5 22 5 13a7 7 0 0113-3 7 7 0 0113 3c0 9-13 18-13 18z" fill="none" stroke="#0292cd" stroke-width="2"/></svg><br>Free health screenings in underserved communities<span class="mini dark">Read more</span></div>
    <div class="do"><svg viewBox="0 0 36 36"><rect x="6" y="12" width="24" height="12" rx="6" fill="none" stroke="#0292cd" stroke-width="2"/><path d="M18 12v12" stroke="#0292cd" stroke-width="2"/></svg><br>Access free or affordable medications<span class="mini">Read more</span></div>
    <div class="do"><svg viewBox="0 0 36 36"><circle cx="18" cy="11" r="6" fill="none" stroke="#0292cd" stroke-width="2"/><path d="M6 32c0-8 5-13 12-13s12 5 12 13" fill="none" stroke="#0292cd" stroke-width="2"/></svg><br>Providers offer a complete physical free once a year<span class="mini">Read more</span></div>
    <div class="do"><svg viewBox="0 0 36 36"><path d="M14 4h8M15 4v10L7 30h22L21 14V4" fill="none" stroke="#0292cd" stroke-width="2"/></svg><br>Assist patients with low cost lab work<span class="mini">Read more</span></div>
  </div>
</section>

<section class="abs programs">
  <h2 class="serif">Successful Worksite Wellness Programs</h2>
  <p class="lead">Healthy employees are feel better and live longer. We've combined the essential components of a successful wellness program into one convenient online package.</p>
  <div class="prog-row">
    <div class="prog"><h4>ASSESS</h4><div class="ph" role="img" aria-label="Photo of a health assessment form" style="background:linear-gradient(135deg,#dfe8ee,#a9bccb)"></div><p>A health risk assessment shows where each person stands today.</p><span class="mini">Read more</span></div>
    <div class="prog"><h4>DISCOVER</h4><div class="ph" role="img" aria-label="Photo of a wellness coaching session" style="background:linear-gradient(135deg,#d9c7b5,#8b9aa6)"></div><p>Personalized reports help members discover their key risks.</p><span class="mini dark">Read more</span></div>
    <div class="prog"><h4>INTERVENE</h4><div class="ph" role="img" aria-label="Photo of a doctor consultation" style="background:linear-gradient(135deg,#e6e1da,#9fb0bd)"></div><p>Targeted programs and coaching address risks early on.</p><span class="mini">Read more</span></div>
    <div class="prog"><h4>MOTIVATE</h4><div class="ph" role="img" aria-label="Photo of a fitness workout" style="background:linear-gradient(135deg,#e3e9ee,#b6c2cc)"></div><p>Members earn points and rewards for completed activities.</p><span class="mini">Read more</span></div>
    <div class="prog"><h4>TRACK</h4><div class="ph" role="img" aria-label="Photo of an activity tracking chart" style="background:linear-gradient(135deg,#f1f1f1,#c8ced3)"></div><p>The activity tracker logs progress toward every health goal.</p><span class="mini">Read more</span></div>
  </div>
</section>

<section class="abs events">
  <h2 class="serif">Latest Events</h2>
  <div class="ev-row">
    <div class="ev"><div class="ph" role="img" aria-label="Photo of a man meditating on a beach" style="background:linear-gradient(180deg,#8fc3e3,#e8dcc0)"></div><h3 class="serif">Consectetur adipiscing</h3><p>Join our sunrise mindfulness session by the lake and learn easy habits for stress relief and better sleep.</p><div class="ev-meta"><span>Aug 6, 2015</span><span>Admin</span><span>0</span></div></div>
    <div class="ev"><div class="ph" role="img" aria-label="Photo of a smiling senior couple" style="background:linear-gradient(135deg,#c8d6c0,#8fa987)"></div><h3 class="serif">Sed ut perspiciatis</h3><p>A free community screening day with blood pressure checks, glucose tests and friendly health advice.</p><div class="ev-meta"><span>Aug 5, 2015</span><span>Admin</span><span>0</span></div></div>
    <div class="ev"><div class="ph" role="img" aria-label="Photo of a caregiver with an elderly patient" style="background:linear-gradient(135deg,#e7ddd0,#a9b6bf)"></div><h3 class="serif">Lorem ipsum dolor</h3><p>Meet local providers and free clinics offering yearly physicals for members who lack insurance.</p><div class="ev-meta"><span>Aug 3, 2015</span><span>Admin</span><span>0</span></div></div>
  </div>
</section>

<section class="abs consult">
  <div class="sub">Your Private Wellness</div>
  <h2 class="serif">Consultation</h2>
  <label>What's your name?</label>
  <div class="field"></div>
  <div class="go">NEXT QUESTION ›</div>
</section>
<div class="abs consult-photo" role="img" aria-label="Photo of a smiling doctor with a mother and child patient"></div>

<section class="abs contact">
  <div class="abs map" role="img" aria-label="Street map showing the office location in Chicago"></div>
  <div class="abs info">
    <h2>Contact</h2>
    <p>Vitoplume is an online wellness center serving Chicago members with tools, screenings and support for better health.</p>
    <div class="line"><svg viewBox="0 0 14 14"><path d="M7 13S2 8 2 5a5 5 0 0110 0c0 3-5 8-5 8z" fill="#0292cd"/><circle cx="7" cy="5" r="1.8" fill="#fff"/></svg><span>Vitoplume<br>2418 Larkspur Ave<br>Chicago, IL 60614</span></div>
    <div class="line"><svg viewBox="0 0 14 14"><path d="M3 1l3 3-2 2a8 8 0 004 4l2-2 3 3-2 2C6 13 1 8 1 3z" fill="#0292cd"/></svg><span>+1 (312) 555-0148</span></div>
    <div class="line"><svg viewBox="0 0 14 14"><rect x="1" y="3" width="12" height="8" fill="none" stroke="#0292cd" stroke-width="1.5"/><path d="M1 3l6 5 6-5" fill="none" stroke="#0292cd" stroke-width="1.5"/></svg><span>hello@vitoplume.com</span></div>
  </div>
</section>

<footer class="abs footer">
  <div class="fname">Vitoplume</div>
  <div class="copy">© 2015 Vitoplume  |  www.vitoplume.com</div>
  <div class="up"></div>
</footer>

</body>
</html>
```